Veradine Contracting Folder

Creating a design for the cover of our folders that we pass to our customers

Want to keep the same look as our colors and fonts as attached

```html
<!DOCTYPE html>
<html lang="en">
<head>
<meta charset="utf-8">
<title>Veradine Contracting Folder Cover</title>
<link rel="stylesheet" href="https://fonts.googleapis.com/css2?family=Arimo:wght@400;700&display=swap">
<style>
  :root {
    --stage: #c9c2f2;
    --paper: #ffffff;
    --lilac: #cbaaf3;
    --royal: #0a0eaf;
    --violet: #5a3ed8;
    --ink: #111111;
  }
  html, body {
    margin: 0;
    padding: 0;
    width: 1200px;
    height: 746px;
    overflow: hidden;
    background: var(--stage);
    font-family: "Arimo", Arial, sans-serif;
  }
  .canvas {
    position: relative;
    width: 1200px;
    height: 746px;
  }
  .folder-cover {
    position: absolute;
    left: 357px;
    top: 26px;
    width: 486px;
    height: 694px;
    background: var(--paper);
    box-shadow: 0 6px 24px rgba(40, 20, 120, 0.18);
  }
  .folder-cover svg { display: block; }
  .brand-name { font-family: "Arimo", Arial, sans-serif; font-weight: 700; fill: var(--royal); }
  .address-title { font-family: "Arimo", Arial, sans-serif; font-weight: 700; font-size: 17px; fill: var(--ink); }
  .address-line { font-family: "Arimo", Arial, sans-serif; font-size: 12.5px; fill: var(--ink); }
  .social-label { font-family: "Arimo", Arial, sans-serif; font-size: 13.5px; fill: var(--paper); }
</style>
</head>
<body>
<main class="canvas">
  <section class="folder-cover" aria-label="Veradine Contracting folder cover">
    <svg width="486" height="694" viewBox="0 0 485 693" xmlns="http://www.w3.org/2000/svg">
      <defs>
        <linearGradient id="ring-gradient" x1="0" y1="0" x2="1" y2="1">
          <stop offset="0" stop-color="#b99af0"/>
          <stop offset="0.5" stop-color="#5a3ed8"/>
          <stop offset="1" stop-color="#1a10c0"/>
        </linearGradient>
        <linearGradient id="skyline-gradient" x1="0" y1="0" x2="1" y2="0">
          <stop offset="0" stop-color="#8a6ee6"/>
          <stop offset="1" stop-color="#1a12b8"/>
        </linearGradient>
        <linearGradient id="band-gradient" x1="0" y1="0" x2="1" y2="0">
          <stop offset="0" stop-color="#c8a8f3"/>
          <stop offset="0.5" stop-color="#6a4ede"/>
          <stop offset="1" stop-color="#0a0eaf"/>
        </linearGradient>
      </defs>

      <g class="brand-lockup">
        <text class="brand-name" x="32" y="88" font-size="44" textLength="196" lengthAdjust="spacingAndGlyphs">VERADINE</text>
        <text class="brand-name" x="48" y="114" font-size="20" letter-spacing="3">Contracting</text>
      </g>

      <g class="geometry">
        <polygon fill="var(--lilac)" points="321,0 443,0 335,188 213,188"/>
        <polygon fill="var(--royal)" points="443,0 485,0 485,140 395,291 335,188"/>
        <polygon fill="var(--lilac)" points="70,217 135,217 70,330"/>
        <polygon fill="var(--royal)" points="415,363 415,476 350,476"/>
        <polygon fill="var(--lilac)" points="0,548 88,400 150,504 65,650 0,650"/>
        <polygon fill="var(--royal)" points="150,504 270,504 186,650 65,650"/>
      </g>

      <path class="hex-frame" fill="url(#ring-gradient)" fill-rule="evenodd"
        d="M93,348 L160,217 L320,217 L392,348 L320,476 L168,476 Z
           M124,348 L185,243 L303,243 L362,348 L296,451 L190,451 Z"/>

      <rect class="city-skyline" role="img" aria-label="City skyline illustration of office towers"
        x="186" y="372" width="134" height="79" fill="url(#skyline-gradient)"/>

      <g class="contact-block">
        <text class="address-title" x="299" y="564">YOUR ADDRESS</text>
        <text class="address-line" x="288" y="587">Your Address Your Address</text>
        <text class="address-line" x="288" y="601">Your Address&#160; Your Address</text>
        <text class="address-line" x="288" y="616">Your Address&#160; Your Address</text>
      </g>

      <g class="social-band">
        <rect x="0" y="656" width="485" height="37" fill="url(#band-gradient)"/>
        <circle cx="30" cy="674.5" r="8.5" fill="var(--paper)"/>
        <text class="social-label" x="48" y="679">Your Social Media</text>
        <circle cx="183" cy="674.5" r="8.5" fill="var(--paper)"/>
        <text class="social-label" x="201" y="679">Your Social Media</text>
        <circle cx="336" cy="674.5" r="8.5" fill="var(--paper)"/>
        <text class="social-label" x="354" y="679">Your Social Media</text>
      </g>
    </svg>
  </section>
</main>
</body>
</html>
```